Postcard Design Project( EDDM 6.5in wide x 9in )

Painting Company
- Interior and Exterior Painting
- Wallpaper Removal and Installation
- Wood Staining
-Licensed and Insured HIC #PA739408
-website: www.miloverhunpainting.com
-Facebook: @verhpainting
-Phone #: 555-218-3064
Fall Special Discount 10% off $500.00 or more
(EDDM Postcard size (6.5in wide x9)

Target Market(s)

People who are in need of painting

Industry/Entity Type

Painting

Requirements
Must have
• Must be bold and make a statement. I need the people to hold on to the postcard and not throw it away.
Should not have
• Should not look like you took it off a template.

```html
<!DOCTYPE html>
<html lang="en">
<head>
<meta charset="utf-8">
<title>Milo Verhun Painting – Fall Special Postcard</title>
<link href="https://fonts.googleapis.com/css2?family=Questrial&family=Rubik:wght@800&display=swap" rel="stylesheet">
<style>
  :root {
    --magenta: #d21c5e;
    --magenta-dark: #a8124a;
    --blue: #1f6bb5;
    --navy: #1e2a6e;
    --yellow: #fff200;
    --white: #ffffff;
    --backdrop: #f1f1f1;
    --photo-light: #eef0f2;
    --photo-mid: #c9d3dc;
  }
  html, body {
    margin: 0;
    padding: 0;
    width: 1200px;
    height: 1200px;
    overflow: hidden;
    background: var(--backdrop);
  }
  .postcard {
    display: block;
    width: 1200px;
    height: 1200px;
  }
  .body-text { font-family: "Questrial", "Century Gothic", sans-serif; }
  .badge-text { font-family: "Rubik", "Arial Black", sans-serif; font-weight: 800; }
  .brand-name { fill: var(--navy); font-family: "Questrial", sans-serif; font-size: 38px; letter-spacing: 1px; }
  .service-item { fill: var(--blue); font-size: 31px; }
  .contact-item { fill: var(--white); font-size: 24px; }
  .footnote { fill: var(--navy); font-size: 18px; }
</style>
</head>
<body>
<svg class="postcard" viewBox="0 0 1500 1500" xmlns="http://www.w3.org/2000/svg">
  <defs>
    <linearGradient id="photoTone" x1="0" y1="0" x2="1" y2="1">
      <stop offset="0" stop-color="var(--photo-light)"/>
      <stop offset="0.6" stop-color="var(--photo-mid)"/>
      <stop offset="1" stop-color="#8fa9c4"/>
    </linearGradient>
    <linearGradient id="strokeTone" x1="0" y1="0" x2="0" y2="1">
      <stop offset="0" stop-color="var(--magenta)"/>
      <stop offset="1" stop-color="var(--magenta-dark)"/>
    </linearGradient>
    <clipPath id="pageClip"><rect x="288" y="65" width="925" height="1370"/></clipPath>
  </defs>

  <!-- Page -->
  <rect class="page" x="288" y="65" width="925" height="1370" fill="var(--white)"/>

  <g class="decor" clip-path="url(#pageClip)">
    <!-- Top-left triangles -->
    <polygon points="288,65 318,65 395,165 288,165" fill="var(--magenta)"/>
    <polygon points="355,65 403,65 378,105" fill="var(--magenta)"/>
    <polygon points="385,122 437,65 490,122" fill="var(--blue)"/>
    <polygon points="440,137 490,137 465,180" fill="var(--magenta)"/>
    <polygon points="300,198 348,198 324,240" fill="var(--magenta)"/>
    <line x1="512" y1="68" x2="535" y2="92" stroke="var(--magenta)" stroke-width="1.5"/>
    <line x1="520" y1="66" x2="540" y2="88" stroke="var(--magenta)" stroke-width="1.5"/>

    <!-- Side wedges -->
    <polygon points="288,240 630,580 288,920" fill="var(--blue)"/>
    <polygon points="1213,240 873,580 1213,920" fill="var(--magenta)"/>

    <!-- Bottom-right triangles -->
    <polygon points="1110,1172 1172,1050 1234,1172" fill="var(--magenta)"/>
    <polygon points="1110,1180 1165,1180 1137,1228" fill="var(--blue)"/>
    <polygon points="1125,1065 1160,1065 1142,1095" fill="var(--blue)"/>
    <polygon points="1096,1070 1110,1070 1103,1058" fill="var(--blue)"/>
    <polygon points="1115,1110 1135,1110 1125,1094" fill="var(--magenta)"/>
    <polygon points="1165,1040 1180,1040 1172,1027" fill="var(--blue)"/>
    <polygon points="1195,1055 1213,1025 1213,1055" fill="var(--magenta)"/>
    <polygon points="1195,1195 1213,1195 1213,1220" fill="var(--magenta)"/>
    <line x1="1090" y1="1185" x2="1125" y2="1125" stroke="var(--magenta)" stroke-width="1.5"/>
    <line x1="1096" y1="1185" x2="1130" y2="1127" stroke="var(--magenta)" stroke-width="1.5"/>
    <line x1="1130" y1="1260" x2="1170" y2="1200" stroke="var(--blue)" stroke-width="1.5"/>
    <line x1="1137" y1="1260" x2="1176" y2="1202" stroke="var(--blue)" stroke-width="1.5"/>
  </g>

  <!-- Brand name -->
  <g class="brand">
    <text class="brand-name" x="1112" y="178" text-anchor="end">MILO VERHUN</text>
    <text class="brand-name" x="1112" y="222" text-anchor="end">PAINTING</text>
    <text class="brand-name" x="1112" y="262" text-anchor="end" style="font-size:17px;letter-spacing:3px">VETERAN OWNED</text>
  </g>

  <!-- Photo diamond -->
  <polygon class="photo-frame" points="750,222 1122,595 750,965 378,595" fill="var(--white)"/>
  <polygon class="photo" role="img" aria-label="Photo of a painter on a ladder rolling white paint onto a ceiling"
           points="750,252 1095,595 750,938 405,595" fill="url(#photoTone)"/>

  <!-- Discount badge -->
  <g class="discount-badge">
    <path d="M390,625 C420,575 520,585 580,600 C640,610 665,660 640,710 C625,740 590,748 540,748
             L512,748 L510,960 C509,985 495,985 494,960 L488,800 C487,780 478,780 477,800
             L474,905 C473,918 462,918 461,905 L455,760 C448,750 440,752 438,770 L436,880
             C435,890 426,890 425,880 L420,745 C385,720 368,670 390,625 Z"
          fill="var(--magenta)"/>
    <text class="badge-text" x="508" y="636" text-anchor="middle" fill="var(--white)" font-size="24">FALL SPECIAL</text>
    <text class="badge-text" x="508" y="663" text-anchor="middle" fill="var(--white)" font-size="24">DISCOUNT</text>
    <text class="badge-text" x="503" y="702" text-anchor="middle" fill="var(--yellow)" font-size="40">10% OFF</text>
    <text class="body-text" x="507" y="727" text-anchor="middle" fill="var(--white)" font-size="21">$500.00 or more</text>
  </g>

  <!-- Services heading -->
  <g class="services-heading">
    <rect role="img" aria-label="Yellow paint roller" x="452" y="998" width="72" height="20" rx="4" fill="#f2d21b"/>
    <rect x="524" y="990" width="476" height="84" fill="url(#strokeTone)"/>
    <text class="body-text" x="750" y="1052" text-anchor="middle" fill="var(--yellow)" font-size="54">OUR SERVICES</text>
  </g>

  <!-- Services list -->
  <g class="services-list body-text">
    <polygon points="502,1103 496,1117 509,1117" fill="var(--magenta)"/>
    <text class="service-item" x="515" y="1122">INTERIOR AND EXTERIOR PAINTING</text>
    <polygon points="452,1140 446,1154 459,1154" fill="var(--magenta)"/>
    <text class="service-item" x="465" y="1159">WALLPAPER REMOVAL AND INSTALLATION</text>
    <polygon points="631,1177 625,1191 638,1191" fill="var(--magenta)"/>
    <text class="service-item" x="644" y="1196">WOOD STAINING</text>
  </g>

  <!-- Contact icons -->
  <g class="contact-icons">
    <circle cx="453" cy="1262" r="24" fill="var(--magenta)"/>
    <rect x="640" y="1240" width="25" height="44" rx="4" fill="none" stroke="var(--magenta)" stroke-width="3"/>
    <line x1="640" y1="1249" x2="665" y2="1249" stroke="var(--magenta)" stroke-width="2"/>
    <line x1="640" y1="1274" x2="665" y2="1274" stroke="var(--magenta)" stroke-width="2"/>
    <circle cx="652.5" cy="1279" r="1.8" fill="var(--magenta)"/>
    <g fill="none" stroke="var(--magenta)" stroke-width="2.5">
      <circle cx="961" cy="1262" r="22"/>
      <ellipse cx="961" cy="1262" rx="10" ry="22"/>
      <line x1="961" y1="1240" x2="961" y2="1284"/>
      <line x1="939" y1="1262" x2="983" y2="1262"/>
      <line x1="943" y1="1250" x2="979" y2="1250"/>
      <line x1="943" y1="1274" x2="979" y2="1274"/>
    </g>
  </g>

  <!-- Contact band -->
  <rect class="contact-band" x="288" y="1298" width="925" height="42" fill="var(--blue)"/>
  <g class="body-text">
    <text class="contact-item" x="446" y="1328" text-anchor="middle">@verhpainting</text>
    <text class="contact-item" x="654" y="1328" text-anchor="middle">555-218-3064</text>
    <text class="contact-item" x="967" y="1328" text-anchor="middle">www.miloverhunpainting.com</text>
    <text class="footnote" x="650" y="1368" text-anchor="middle">Licensed and Insured</text>
    <text class="footnote" x="776" y="1368" text-anchor="middle">|</text>
    <text class="footnote" x="876" y="1368" text-anchor="middle">Veteran Owned</text>
  </g>
</svg>
</body>
</html>
```